Online bill payment portal website design

Online Invoice Payment Website

The customer will click on the logos of the institution they want to pay and the payment will be made at the latest stage to write the customer number.

Invoice payment can be made online. Telephone, Television, Internet, Electricity, Water, Natural Gas, and all institutional payments.

Example website : https://www.selvopay.com/

Industry/Entity Type

Invoice

Logo Text

KolayBorcKapat.Net

Number of Pages Required

4 page

Font styles to use
Serif
Sans Serif

Colors
abd036
33a6d7
876aae
e667a6
ec1f27
f37122
85abd2
0555a3
00a990

Requirements
Must have
• Logos of payment institutions
• Credit Card Payment form
• Customer information form
• COntact page
• List of Institutions
• Accept privacy policies in all forms
Nice to have
• Good and new design :)
Should not have
• Same with selvopay.com ! i want new site

```html
<!DOCTYPE html>
<html lang="en">
<head>
<meta charset="utf-8">
<title>Online Bill Payment</title>
<link href="https://fonts.googleapis.com/css2?family=Montserrat:wght@400;500;600;700&display=swap" rel="stylesheet">
<style>
  :root {
    --brand-blue: #0555a3;
    --brand-blue-dark: #003c86;
    --bright-blue: #0a72e0;
    --ink: #333333;
    --text-grey: #777777;
    --icon-grey: #a9a9a9;
    --panel-grey: #f0f0f0;
    --white: #ffffff;
    --bar-grey: #a4a8b0;
    --circle-blue: #044a90;
  }
  * { box-sizing: border-box; margin: 0; padding: 0; }
  html, body { width: 1200px; height: 1147px; overflow: hidden; }
  body { font-family: "Montserrat", Arial, sans-serif; color: var(--ink); background: var(--white); position: relative; }
  section, header, footer { position: absolute; left: 0; width: 1200px; }
  .abs { position: absolute; }

  .site-header { top: 0; height: 111px; background: var(--white); }
  .logo { left: 29px; top: 38px; font-size: 27px; font-weight: 700; color: var(--brand-blue); letter-spacing: 0.5px; }
  .main-nav { left: 176px; top: 45px; display: flex; gap: 22px; font-size: 16.5px; font-weight: 500; color: var(--ink); }
  .main-nav .active { font-weight: 700; }
  .header-login { left: 995px; top: 45px; font-size: 16.5px; font-weight: 700; color: var(--brand-blue); }
  .btn { display: flex; align-items: center; justify-content: center; font-weight: 700; font-size: 17px; }
  .btn-solid { background: var(--brand-blue); color: var(--white); border-radius: 2px; }
  .btn-outline { border: 2px solid var(--brand-blue); color: var(--brand-blue); border-radius: 2px; background: var(--white); }
  .header-signup { left: 1057px; top: 33px; width: 114px; height: 45px; }

  .hero { top: 111px; height: 252px; background: linear-gradient(160deg, #0a5fb0 0%, var(--brand-blue) 45%, var(--brand-blue-dark) 100%); color: var(--white); }
  .hero-title { left: 31px; top: 36px; font-size: 28px; font-weight: 700; }
  .hero-text { left: 32px; top: 71px; font-size: 18px; line-height: 23px; font-weight: 500; }
  .hero-login { left: 33px; top: 155px; width: 84px; height: 46px; border: 2px solid var(--white); color: var(--white); }
  .hero-or { left: 130px; top: 166px; font-size: 18px; font-weight: 700; }
  .hero-signup { left: 170px; top: 155px; width: 169px; height: 46px; background: var(--bright-blue); color: var(--white); border-radius: 2px; }

  .services { top: 363px; height: 110px; background: var(--white); }
  .services-label { right: 780px; top: 32px; text-align: right; font-size: 17px; line-height: 21px; font-weight: 700; color: var(--brand-blue); }
  .service { top: 18px; width: 110px; margin-left: -55px; text-align: center; color: var(--text-grey); font-size: 16.5px; font-weight: 500; }
  .service svg { display: block; margin: 0 auto 6px; height: 44px; }

  .partners { top: 473px; height: 175px; background: var(--panel-grey); }
  .partners-title { left: 32px; top: 19px; font-size: 17px; font-weight: 700; color: var(--brand-blue); }
  .partners-all { right: 30px; top: 19px; font-size: 17px; font-weight: 700; color: #555; }
  .partner-card { top: 53px; width: 216px; height: 79px; background: var(--white); border-radius: 3px; box-shadow: 0 1px 3px rgba(0,0,0,0.15); display: flex; align-items: center; justify-content: center; font-size: 21px; font-weight: 700; color: #8e8e8e; }
  .partner-card.faded { width: 200px; justify-content: flex-start; padding-left: 33px; overflow: hidden; -webkit-mask-image: linear-gradient(90deg, #000 45%, transparent 100%); mask-image: linear-gradient(90deg, #000 45%, transparent 100%); }
  .scroll-bar { left: 28px; top: 154px; width: 305px; height: 12px; border-radius: 3px; background: var(--bar-grey); }

  .about { top: 648px; height: 340px; background: var(--white); }
  .about-title { left: 32px; top: 20px; font-size: 17px; font-weight: 700; color: #444; }
  .about-text { left: 32px; top: 45px; width: 690px; font-size: 16.8px; line-height: 21px; color: var(--text-grey); }
  .about-text p + p { margin-top: 21px; }
  .video-panel { left: 755px; top: 49px; width: 416px; height: 273px; background: var(--brand-blue); border-radius: 2px; }
  .video-title { left: 22px; top: 16px; font-size: 17px; font-weight: 700; color: var(--white); }
  .video-play { left: 166px; top: 96px; width: 84px; height: 84px; border-radius: 50%; background: var(--circle-blue); }

  .site-footer { top: 988px; height: 159px; background: var(--panel-grey); }
  .secure { left: 29px; top: 26px; display: flex; align-items: center; gap: 14px; font-size: 17px; line-height: 20px; font-weight: 700; color: var(--brand-blue); }
  .legal { left: 32px; top: 89px; font-size: 15px; line-height: 24px; font-weight: 600; color: #444; }
  .payment-methods { right: 29px; top: 26px; display: flex; gap: 24px; font-size: 20px; font-weight: 700; color: var(--brand-blue); }
  .footer-login { left: 948px; top: 81px; width: 93px; height: 45px; }
  .footer-signup { left: 1057px; top: 81px; width: 114px; height: 45px; }
</style>
</head>
<body>

<header class="site-header">
  <div class="abs logo">LOGO</div>
  <nav class="abs main-nav">
    <span class="active">Home</span><span>Companies</span><span>About</span><span>Privacy policies</span><span>Contact us</span>
  </nav>
  <div class="abs header-login">Login</div>
  <div class="abs btn btn-solid header-signup">Sign up</div>
</header>

<section class="hero">
  <h1 class="abs hero-title">Save time</h1>
  <p class="abs hero-text">Lorem ipsum dolor sit amet,<br>consectetur adipiscing elit<br>etiam sollicitudin nisi id porttitor.</p>
  <div class="abs btn hero-login">login</div>
  <div class="abs hero-or">or</div>
  <div class="abs btn hero-signup">¡sign up now!</div>
</section>

<section class="services">
  <div class="abs services-label">Services that you<br>can pay here:</div>
  <div class="abs service" style="left:506px">
    <svg viewBox="0 0 50 44" width="50"><rect x="1" y="2" width="48" height="30" rx="2" fill="var(--icon-grey)"/><rect x="1" y="26" width="48" height="6" fill="#c4c4c4"/><rect x="21" y="32" width="8" height="7" fill="var(--icon-grey)"/><rect x="13" y="39" width="24" height="3" fill="var(--icon-grey)"/></svg>Television</div>
  <div class="abs service" style="left:626px">
    <svg viewBox="0 0 48 44" width="48"><rect x="1" y="1" width="11" height="42" rx="4" fill="var(--icon-grey)"/><rect x="14" y="6" width="32" height="36" rx="3" fill="none" stroke="var(--icon-grey)" stroke-width="3"/><rect x="20" y="11" width="20" height="6" fill="var(--icon-grey)"/><g fill="var(--icon-grey)"><rect x="20" y="21" width="5" height="4"/><rect x="28" y="21" width="5" height="4"/><rect x="36" y="21" width="5" height="4"/><rect x="20" y="28" width="5" height="4"/><rect x="28" y="28" width="5" height="4"/><rect x="36" y="28" width="5" height="4"/><rect x="20" y="35" width="5" height="4"/><rect x="28" y="35" width="5" height="4"/><rect x="36" y="35" width="5" height="4"/></g></svg>Telephone</div>
  <div class="abs service" style="left:717px">
    <svg viewBox="0 0 36 50" width="32" style="height:48px;margin-bottom:2px"><path d="M18 2 C24 14 34 20 34 34 C34 43 27 49 18 49 C9 49 2 43 2 34 C2 26 8 22 10 14 C14 20 14 24 14 28 C18 20 20 12 18 2 Z" fill="none" stroke="var(--icon-grey)" stroke-width="3"/><path d="M18 30 C22 36 26 38 26 42 C26 46 22 48 18 48 C14 48 11 46 11 42 C11 38 15 36 18 30 Z" fill="var(--icon-grey)"/></svg>Gas</div>
  <div class="abs service" style="left:809px">
    <svg viewBox="0 0 50 44" width="50"><circle cx="25" cy="22" r="20" fill="none" stroke="var(--icon-grey)" stroke-width="3"/><circle cx="25" cy="22" r="13" fill="none" stroke="var(--icon-grey)" stroke-width="3"/><rect x="19" y="10" width="3" height="8" fill="var(--icon-grey)"/><rect x="28" y="10" width="3" height="8" fill="var(--icon-grey)"/><path d="M16 17 H34 V22 C34 27 30 30 25 30 C20 30 16 27 16 22 Z" fill="var(--icon-grey)"/><rect x="23" y="29" width="4" height="10" fill="var(--icon-grey)"/></svg>Electricity</div>
  <div class="abs service" style="left:907px">
    <svg viewBox="0 0 36 44" width="34"><path d="M18 2 C24 12 33 20 33 29 C33 37 26 42 18 42 C10 42 3 37 3 29 C3 20 12 12 18 2 Z" fill="none" stroke="var(--icon-grey)" stroke-width="3"/><path d="M4 28 C12 24 24 32 32 27 C32 36 26 41 18 41 C10 41 4 36 4 28 Z" fill="var(--icon-grey)"/></svg>Water</div>
</section>

<section class="partners">
  <div class="abs partners-title">Some of our partners</div>
  <div class="abs partners-all">see all companies</div>
  <div class="abs partner-card" style="left:29px">LOGO BRAND</div>
  <div class="abs partner-card" style="left:266px">LOGO BRAND</div>
  <div class="abs partner-card" style="left:503px">LOGO BRAND</div>
  <div class="abs partner-card" style="left:740px">LOGO BRAND</div>
  <div class="abs partner-card faded" style="left:977px">LOGO BRAND</div>
  <div class="abs scroll-bar"></div>
</section>

<section class="about">
  <h2 class="abs about-title">About us and service</h2>
  <div class="abs about-text">
    <p>Lorem ipsum dolor sit amet, consectetur adipiscing elit. In sit amet arcu a purus imperdiet scelerisque nec sit amet mauris. Maecenas scelerisque dui et tortor semper, eget tempus dolor pulvinar. Mauris iaculis mauris non nisi sagittis, ac bibendum elit lobortis. Mauris tempus ipsum vel lorem pretium, vel convallis justo ultricies.</p>
    <p>Integer id mauris vel mi viverra tincidunt sollicitudin non diam. Sed aliquam nisi vitae odio fringilla lacinia. Suspendisse condimentum turpis malesuada augue iaculis mollis. Phasellus non condimentum quam, sed tempor dui. Pellentesque egestas vestibulum magna id dignissim.</p>
  </div>
  <div class="abs video-panel" role="img" aria-label="Video presentation player">
    <div class="abs video-title">Video presentation</div>
    <div class="abs video-play"></div>
  </div>
</section>

<footer class="site-footer">
  <div class="abs secure">
    <svg width="46" height="46" viewBox="0 0 46 46"><circle cx="23" cy="23" r="22" fill="var(--brand-blue)"/><path d="M23 10 L33 14 V22 C33 29 28 34 23 36 C18 34 13 29 13 22 V14 Z" fill="var(--white)"/><path d="M18 23 L22 27 L29 19" fill="none" stroke="var(--brand-blue)" stroke-width="3"/></svg>
    <span>Secure<br>website</span>
  </div>
  <p class="abs legal">All rights reserved. Copyright(c) 2017<br>Selvo, 6493 sayılı kanun kapsamında 12.04.2016 tarihi itibarıyla.</p>
  <div class="abs payment-methods"><span>Paywell</span><span>Vantra</span><span>Meridian</span></div>
  <div class="abs btn btn-outline footer-login">Login</div>
  <div class="abs btn btn-solid footer-signup">Sign up</div>
</footer>

</body>
</html>
```